Business Card Design Project

Looking to get a new business card design for a 16pt matte finish and spot UV front and back. The designs I'm looking for would be a black background with our logo incorporated somehow and three different color ink swirls/splatters for pink, yellow, blue. a design inspiration would be a card that www.plankvoro.com did for his business card.
Updates

I've added some sample cards in my files to show the direction I'd like to go in.

Target Market(s)

upscale automotive industry

Industry/Entity Type

Business

Requirements
Must have
• logo
ink vapor swirl and or splatter in either black or three colors, pink, yellow, blue
Should not have
• normal everyday business card

```html
<!DOCTYPE html>
<html lang="en">
<head>
<meta charset="utf-8">
<title>Norvel Motors – Business Card</title>
<link rel="stylesheet" href="https://fonts.googleapis.com/css2?family=Montserrat:wght@400;500;600;700&display=swap">
<style>
  :root {
    --bg: #e9e9e9;
    --card: #0c0c0c;
    --white: #f2f2f2;
    --grey: #bdbdbd;
    --rule: #5a5a5a;
    --red: #e0222b;
    --ink-pink: rgba(236, 64, 160, .55);
    --ink-yellow: rgba(250, 214, 60, .45);
    --ink-blue: rgba(40, 150, 235, .55);
  }
  * { box-sizing: border-box; margin: 0; padding: 0; }
  html, body {
    width: 1200px; height: 1015px; overflow: hidden;
    background: var(--bg);
    font-family: "Montserrat", Arial, sans-serif;
  }
  .sheet {
    position: relative; width: 1200px; height: 1015px;
    display: flex; flex-direction: column; align-items: center; justify-content: center; gap: 70px;
  }
  .card {
    position: relative; width: 660px; height: 377px;
    background: var(--card);
    box-shadow: 0 14px 30px rgba(0,0,0,.25);
    color: var(--white);
    overflow: hidden;
  }
  .ink-vapor {
    position: absolute; pointer-events: none;
    filter: blur(6px);
  }
  .card-front .ink-vapor {
    inset: 0;
    background:
      radial-gradient(ellipse 150px 90px at 70px 300px, var(--ink-pink), transparent 70%),
      radial-gradient(ellipse 120px 70px at 150px 340px, var(--ink-yellow), transparent 70%),
      radial-gradient(ellipse 170px 80px at 600px 60px, var(--ink-blue), transparent 70%),
      radial-gradient(ellipse 90px 60px at 520px 30px, var(--ink-pink), transparent 70%);
  }
  .card-back .ink-vapor {
    left: 0; top: 0; width: 300px; height: 210px;
    background:
      radial-gradient(ellipse 130px 80px at 80px 60px, var(--ink-blue), transparent 70%),
      radial-gradient(ellipse 110px 60px at 190px 40px, var(--ink-pink), transparent 70%),
      radial-gradient(ellipse 100px 55px at 120px 140px, var(--ink-yellow), transparent 70%);
  }
  .brand {
    position: absolute; z-index: 1; display: flex; align-items: center; gap: 12px;
    font-weight: 600; color: var(--white); letter-spacing: .5px; white-space: nowrap;
  }
  .brand-dot { width: 14px; height: 14px; border-radius: 50%; background: var(--red); flex: none; }
  .card-front .brand { left: 50%; top: 50%; transform: translate(-50%, -50%); font-size: 34px; }
  .card-back .brand { right: 48px; top: 62px; font-size: 28px; }
  .divider { position: absolute; height: 1px; background: var(--rule); }
  .divider-main { left: 250px; right: 40px; top: 150px; }
  .contact-block { position: absolute; z-index: 1; left: 46px; top: 228px; }
  .person-name { color: var(--red); font-weight: 700; font-size: 21px; line-height: 1.1; }
  .person-title { color: var(--white); font-weight: 500; font-size: 13px; margin-top: 4px; }
  .divider-short { position: static; width: 210px; margin: 12px 0 10px; }
  .contact-list { list-style: none; }
  .contact-list li {
    display: flex; align-items: center; gap: 12px;
    font-size: 13px; color: var(--grey); line-height: 22px; white-space: nowrap;
  }
  .contact-list svg { width: 13px; height: 13px; flex: none; }
</style>
</head>
<body>
<main class="sheet">
  <section class="card card-front" aria-label="Card front">
    <div class="ink-vapor" role="img" aria-label="Spot UV ink vapour swirls and splatters in pink, yellow and blue"></div>
    <div class="brand"><span class="brand-dot"></span>Norvel Motors</div>
  </section>

  <section class="card card-back" aria-label="Card back">
    <div class="ink-vapor" role="img" aria-label="Ink vapour swirls in blue, pink and yellow"></div>
    <div class="brand"><span class="brand-dot"></span>Norvel Motors</div>
    <div class="divider divider-main"></div>
    <div class="contact-block">
      <p class="person-name">Dario Kestrel</p>
      <p class="person-title">Director / Executive Chef</p>
      <div class="divider divider-short"></div>
      <ul class="contact-list">
        <li>
          <svg viewBox="0 0 16 16" aria-hidden="true"><path fill="#e0222b" d="M3 1h3l1.5 4-2 1.2a9 9 0 0 0 4.3 4.3L11 8.5l4 1.5v3a2 2 0 0 1-2 2A12 12 0 0 1 1 3a2 2 0 0 1 2-2z"/></svg>
          000.000.0000
        </li>
        <li>
          <svg viewBox="0 0 16 16" aria-hidden="true"><rect x="1" y="3" width="14" height="10" rx="1" fill="none" stroke="#e0222b" stroke-width="1.6"/><path d="M1.5 4l6.5 5 6.5-5" fill="none" stroke="#e0222b" stroke-width="1.6"/></svg>
          dario@norvelmotors.com
        </li>
        <li>
          <svg viewBox="0 0 16 16" aria-hidden="true"><circle cx="8" cy="8" r="6.5" fill="none" stroke="#e0222b" stroke-width="1.5"/><ellipse cx="8" cy="8" rx="3" ry="6.5" fill="none" stroke="#e0222b" stroke-width="1.2"/><path d="M1.5 8h13" stroke="#e0222b" stroke-width="1.2"/></svg>
          www.norvelmotors.com
        </li>
      </ul>
    </div>
  </section>
</main>
</body>
</html>
```